Summit Glossfloor & Honing
I'm looking for a business card and logo design for my
new Polished Concrete & Grinding business,
If you were to look up Summit in the dictionary it would
say, first in importance, order, or position; leading.
Polished Concrete floors are a niche market, that are being used currently in Shopping centres, office spaces and by most high end architects, builders and designers.
i need my business card & logo to stand out from my
competitors, i need my design + logo to reflect this it
needs to be simple, professional, eye catching, easy
to read and scream quality. The logo will need to be
suitable for a whole range of applications including,
uniforms, letter heads, stickers, and eventually
incorporating in vehicle vinyl wrapping.
Target Market(s)
Builders, architects, Interior designers & home owners
Contact Information for Business Card
Front side:
- Summit Glossfloor & Honing.
- Logo
Rear side:
- Liam Varga
- 0491735082
- info@summitgfh.com.au
- commercial - domestic - industrial
- (later down the line website & space for
social media links
www.summitglossfloor.com.au)
Colors
Designer to choose colors to be used in the design.
Look and feel

```html
<!DOCTYPE html>
<html lang="en">
<head>
<meta charset="utf-8">
<title>Liam Varga – Summit Glossfloor &amp; Honing</title>
<link rel="stylesheet" href="https://fonts.googleapis.com/css2?family=Jost:wght@300;400;700&display=swap">
<style>
  :root {
    --navy: #0e365a;
    --navy-faint: #2a4a6c;
    --gold: #d3a92a;
    --white: #ffffff;
    --rule: #c9d1da;
  }
  html, body {
    margin: 0;
    padding: 0;
    width: 1200px;
    height: 777px;
    overflow: hidden;
    background: var(--navy);
  }
  .card {
    position: relative;
    width: 1200px;
    height: 777px;
    background: var(--navy);
    font-family: "Jost", "Helvetica Neue", Arial, sans-serif;
    color: var(--white);
    overflow: hidden;
  }
  .card__texture {
    position: absolute;
    inset: 0;
    background: linear-gradient(135deg, #10395e 0%, #0d3457 100%);
  }
  .card__watermark {
    position: absolute;
    left: 395px;
    top: 250px;
    margin: 0;
    font-weight: 700;
    font-size: 230px;
    line-height: 1;
    letter-spacing: 4px;
    color: var(--navy-faint);
    white-space: nowrap;
  }
  .holder-name {
    position: absolute;
    left: 105px;
    top: 158px;
    margin: 0;
    font-size: 70px;
    line-height: 1;
    letter-spacing: 6px;
    text-transform: uppercase;
    white-space: nowrap;
  }
  .holder-name__first { font-weight: 300; }
  .holder-name__last { font-weight: 700; margin-left: 14px; }
  .contact-rule {
    position: absolute;
    left: 179px;
    top: 287px;
    width: 2px;
    height: 255px;
    background: var(--rule);
  }
  .contact-icon {
    position: absolute;
    fill: var(--gold);
  }
  .contact-icon--phone { left: 104px; top: 290px; width: 46px; height: 44px; }
  .contact-icon--mail  { left: 104px; top: 378px; width: 46px; height: 34px; }
  .contact-icon--web   { left: 100px; top: 479px; width: 52px; height: 52px; }
  .contact-line {
    position: absolute;
    left: 215px;
    margin: 0;
    font-weight: 300;
    font-size: 36px;
    line-height: 1;
    letter-spacing: 2.6px;
    white-space: nowrap;
  }
  .contact-line--phone   { top: 298px; }
  .contact-line--email   { top: 372px; }
  .contact-line--sectors { top: 417px; }
  .contact-line--web     { top: 490px; }
  .social-links {
    position: absolute;
    left: 105px;
    top: 664px;
    display: flex;
    gap: 40px;
    margin: 0;
    padding: 0;
    list-style: none;
  }
  .social-links__item {
    display: flex;
    align-items: center;
    gap: 10px;
    font-weight: 400;
    font-size: 22px;
    letter-spacing: 1px;
    color: var(--gold);
  }
  .social-links__mark {
    width: 26px;
    height: 26px;
    border-radius: 5px;
    background: var(--gold);
  }
</style>
</head>
<body>
  <main class="card">
    <div class="card__texture" role="img" aria-label="Fine diamond lattice texture in muted grey over navy"></div>
    <p class="card__watermark" aria-hidden="true">Summit</p>

    <h1 class="holder-name"><span class="holder-name__first">Liam</span><span class="holder-name__last">Varga</span></h1>

    <div class="contact-rule"></div>

    <svg class="contact-icon contact-icon--phone" viewBox="0 0 24 24" aria-hidden="true">
      <path d="M6.6 2.2c.6-.4 1.4-.3 1.8.3l2.3 3.4c.4.6.3 1.4-.2 1.9L9 9.3c1.1 2.4 3.2 4.5 5.7 5.7l1.5-1.5c.5-.5 1.3-.6 1.9-.2l3.4 2.3c.6.4.7 1.2.3 1.8l-1.5 2.2c-.6.9-1.7 1.3-2.7 1C10.6 18.7 5.3 13.4 3.4 6.4c-.3-1 .1-2.1 1-2.7z"/>
    </svg>
    <p class="contact-line contact-line--phone">0491735082</p>

    <svg class="contact-icon contact-icon--mail" viewBox="0 0 46 34" aria-hidden="true">
      <path d="M0 0h46L23 19z"/>
      <path d="M0 4l23 19L46 4v30H0z"/>
    </svg>
    <p class="contact-line contact-line--email">info@summitgfh.com.au</p>
    <p class="contact-line contact-line--sectors">Commercial &nbsp;| &nbsp;Domestic &nbsp;| &nbsp;Industrial</p>

    <svg class="contact-icon contact-icon--web" viewBox="0 0 52 52" aria-hidden="true">
      <path fill-rule="evenodd" d="M26 0a26 26 0 1 1 0 52A26 26 0 0 1 26 0zm-3 4.3C19.5 8.3 17.6 12 17 16h6zm6 0V16h6c-.6-4-2.5-7.7-6-11.7zM17.9 5.8A22 22 0 0 0 7.5 16h5.5c.6-3.7 2.1-7 4.9-10.2zm16.2 0c2.8 3.2 4.3 6.5 4.9 10.2h5.5A22 22 0 0 0 34.1 5.8zM5.6 21a21 21 0 0 0 0 10h6.8a50 50 0 0 1 0-10zm11.8 0a45 45 0 0 0 0 10H23V21zm11.6 0v10h5.6a45 45 0 0 0 0-10zm10.6 0a50 50 0 0 1 0 10h6.8a21 21 0 0 0 0-10zM7.5 36a22 22 0 0 0 10.4 10.2c-2.8-3.2-4.3-6.5-4.9-10.2zm9.5 0c.6 4 2.5 7.7 6 11.7V36zm12 0v11.7c3.5-4 5.4-7.7 6-11.7zm10 0c-.6 3.7-2.1 7-4.9 10.2A22 22 0 0 0 44.5 36z"/>
    </svg>
    <p class="contact-line contact-line--web">www.summitglossfloor.com.au</p>

    <ul class="social-links">
      <li class="social-links__item"><span class="social-links__mark"></span>Snapvue</li>
      <li class="social-links__item"><span class="social-links__mark"></span>Kinnect</li>
      <li class="social-links__item"><span class="social-links__mark"></span>Chirpline</li>
    </ul>
  </main>
</body>
</html>
```